Strong, modern, clean Business Card design

Looking for a stunning, but CLEAN business card design. While we are a faith-based organization, we do NOT want this to look religious.

Industry/Entity Type

Non-Profit

Contact Information for Business Card

Dale Munroe | Lead Pastor
dale@BrightHarvestHope.org
970-555-0148
PO Box 7316
Millbrook, NE 80571

Font styles to use
Serif
Sans Serif

Requirements
Should not have
• Religious imagery or symbolism

```html
<!DOCTYPE html>
<html lang="en">
<head>
<meta charset="utf-8">
<title>Dale Munroe – Business Card</title>
<link rel="stylesheet" href="https://fonts.googleapis.com/css2?family=Montserrat:wght@300;700&family=Quicksand:wght@400&family=Playfair+Display:wght@700&display=swap">
<style>
  :root {
    --page: #ffffff;
    --card: #4e7b96;
    --ink: #ffffff;
    --ink-soft: #e6e9ec;
  }
  * { margin: 0; padding: 0; box-sizing: border-box; }
  html, body { width: 1200px; height: 1200px; overflow: hidden; background: var(--page); }
  .canvas { position: relative; width: 1200px; height: 1200px; }
  .card {
    position: absolute; left: 172px; top: 415px; width: 839px; height: 479px;
    background: var(--card); color: var(--ink);
  }
  .brand { position: absolute; left: 60px; top: 159px; width: 268px; text-align: center; }
  .brand-square {
    display: block; width: 104px; height: 104px; margin: 0 auto 26px;
    background: var(--ink); border-radius: 14px;
  }
  .brand-name {
    font-family: "Playfair Display", Georgia, serif; font-weight: 700; color: var(--ink);
    font-size: 25px; line-height: 1; letter-spacing: 1px;
  }
  .brand-name .brand-sub { display: block; font-size: 16px; letter-spacing: 12px; margin-top: 8px; padding-left: 12px; }
  .divider { position: absolute; left: 368px; top: 101px; width: 1.5px; height: 280px; background: var(--ink-soft); }
  .person { position: absolute; left: 400px; top: 110px; }
  .person-name {
    font-family: "Montserrat", Arial, sans-serif; font-size: 43px; line-height: 1;
    color: var(--ink-soft); letter-spacing: -1px; white-space: nowrap;
  }
  .person-name .first { font-weight: 700; }
  .person-name .last { font-weight: 300; }
  .person-role {
    font-family: "Montserrat", Arial, sans-serif; font-weight: 300; font-size: 15px;
    letter-spacing: 12px; color: var(--ink-soft); margin-top: 6px; padding-left: 5px;
  }
  .contact { position: absolute; left: 400px; top: 225px; list-style: none; }
  .contact-item {
    display: flex; align-items: center; height: 52px; white-space: nowrap;
    font-family: "Quicksand", Arial, sans-serif; font-size: 21px; color: var(--ink-soft);
  }
  .contact-icon { width: 30px; height: 42px; margin-right: 28px; flex: none; }
</style>
</head>
<body>
<main class="canvas">
  <section class="card">
    <div class="brand">
      <span class="brand-square"></span>
      <p class="brand-name">HARBOR LIGHT<span class="brand-sub">COMMONS</span></p>
    </div>

    <div class="divider"></div>

    <header class="person">
      <h1 class="person-name"><span class="first">DALE</span> <span class="last">MUNROE</span></h1>
      <p class="person-role">LEAD PASTOR</p>
    </header>

    <ul class="contact">
      <li class="contact-item">
        <svg class="contact-icon" viewBox="0 0 30 42" fill="none" stroke="#e6e9ec" stroke-width="1.4" aria-hidden="true">
          <rect x="3" y="1" width="24" height="40" rx="3"/>
          <line x1="3" y1="6" x2="27" y2="6"/>
          <line x1="3" y1="35" x2="27" y2="35"/>
          <line x1="12" y1="38" x2="18" y2="38"/>
        </svg>
        970-555-0148
      </li>
      <li class="contact-item">
        <svg class="contact-icon" viewBox="0 0 30 42" fill="none" stroke="#e6e9ec" stroke-width="1.4" aria-hidden="true">
          <circle cx="15" cy="21" r="6"/>
          <path d="M21 15v8c0 3 5 3 5-2a11 11 0 1 0-5 9"/>
        </svg>
        dale@BrightHarvestHope.org
      </li>
      <li class="contact-item">
        <svg class="contact-icon" viewBox="0 0 30 42" fill="none" stroke="#e6e9ec" stroke-width="1.4" aria-hidden="true">
          <path d="M15 38C8 30 2 24 2 16a13 13 0 0 1 26 0c0 8-6 14-13 22z"/>
          <circle cx="15" cy="16" r="6"/>
        </svg>
        PO Box 7316 Millbrook, NE 80571
      </li>
    </ul>
  </section>
</main>
</body>
</html>
```